Business card / stationery design
Pemberton Hale Warrick
Project: Business card / stationery design
Business card / stationery design - Engineering
Creative Brief
Use specific fonts
Gill Sans MT, Calibri, Corbel, Lucida Sans UC or similar
Professional
Derek R. Pemberton, P.E., LEED A.P., CPMP
Principal
4738 E. Harrowgate Ave., Suite C-212B, Springfield, Missouri 65809
dpemberton@pembertonhalewarrick.example
www.pembertonhalewarrick.example
We would like to use only the logo from the attached file. We like the current color arrangement, but would be interested in seeing it in other colors. Also the slightly gray color behind the logo should just be white or whatever the background color is. A couple of examples are attached. The main text adjacent to the logo should read: Pemberton Hale Warrick. Secondary text will be similar to: Engineering & Energy Services.
We are interested in your ideas.

```html
<!DOCTYPE html>
<html lang="en">
<head>
<meta charset="utf-8">
<title>Pemberton Hale Warrick — Stationery</title>
<link href="https://fonts.googleapis.com/css2?family=Cabin:wght@400;600&display=swap" rel="stylesheet">
<style>
  :root {
    --backdrop: #a7a7a9;
    --paper: #ffffff;
    --brand-green: #7ab843;
    --brand-green-light: #a9d26f;
    --brand-blue: #1f6fa8;
    --ink: #4a4a4a;
    --ink-soft: #7a7a7a;
    --fold: #c9c9c9;
    --mark-faint: #e6edf2;
  }
  * { box-sizing: border-box; margin: 0; padding: 0; }
  html, body { width: 1200px; height: 684px; overflow: hidden; }
  body {
    background: var(--backdrop);
    font-family: "Cabin", "Gill Sans", sans-serif;
    color: var(--ink);
    position: relative;
  }
  .sheet {
    position: absolute;
    background: var(--paper);
    box-shadow: 0 1px 3px rgba(0,0,0,.25);
    overflow: hidden;
  }
  .brand { display: flex; align-items: center; gap: 5px; position: absolute; }
  .brand-square { background: var(--brand-green); display: block; }
  .brand-name {
    font-weight: 600;
    color: var(--ink);
    text-transform: uppercase;
    letter-spacing: .04em;
    white-space: nowrap;
  }
  .band { position: absolute; left: 0; right: 0; display: block; }
  .contact { position: absolute; font-size: 5.5px; line-height: 1.55; color: var(--ink-soft); white-space: nowrap; }
  .web { position: absolute; font-size: 5.5px; color: var(--brand-green); white-space: nowrap; }
  .faint-mark { position: absolute; border: 3px solid var(--mark-faint); background: rgba(230,237,242,.35); }

  /* letterhead */
  .letterhead { left: 192px; top: 24px; width: 374px; height: 653px; }
  .letterhead .brand { left: 24px; top: 26px; }
  .letterhead .brand-square { width: 16px; height: 16px; }
  .letterhead .brand-name { font-size: 8px; }
  .letterhead .contact { left: 24px; top: 604px; }
  .letterhead .band { bottom: 14px; height: 10px; }
  .letterhead .web { left: 24px; bottom: 3px; }
  .letterhead .faint-mark { right: 36px; bottom: 46px; width: 68px; height: 68px; }

  /* business cards */
  .card { width: 187px; height: 101px; left: 96px; }
  .card-front { top: 245px; }
  .card-back { top: 360px; }
  .card .brand { left: 10px; top: 12px; }
  .card .brand-square { width: 14px; height: 14px; }
  .card .brand-name { font-size: 6.5px; }
  .card .band { bottom: 6px; height: 8px; }
  .card-front .web { right: 10px; bottom: 18px; }
  .card-back .holder { position: absolute; left: 10px; top: 34px; font-size: 5.5px; line-height: 1.5; color: var(--ink); white-space: nowrap; }
  .card-back .holder strong { font-weight: 600; }
  .card-back .contact { left: 10px; top: 54px; font-size: 4.8px; }

  /* flap envelope */
  .envelope-flap { left: 643px; top: 96px; width: 468px; height: 250px; }
  .envelope-flap svg.fold { position: absolute; inset: 0; }
  .envelope-flap .brand-square { position: absolute; left: 224px; top: 30px; width: 20px; height: 20px; }

  /* DL envelope */
  .envelope-dl { left: 643px; top: 367px; width: 468px; height: 233px; }
  .envelope-dl .brand { left: 24px; top: 82px; }
  .envelope-dl .brand-square { width: 16px; height: 16px; }
  .envelope-dl .brand-name { font-size: 8px; }
  .envelope-dl .contact { left: 24px; top: 182px; }
  .envelope-dl .band { bottom: 10px; height: 10px; }
  .envelope-dl .faint-mark { right: 22px; top: 100px; width: 86px; height: 86px; }
</style>
</head>
<body>

<svg width="0" height="0" style="position:absolute">
  <defs>
    <linearGradient id="greenFade" x1="0" x2="1">
      <stop offset="0" stop-color="#7ab843"/>
      <stop offset="1" stop-color="#a9d26f"/>
    </linearGradient>
    <symbol id="brand-band" viewBox="0 0 100 10" preserveAspectRatio="none">
      <rect x="0" y="0" width="100" height="1.2" fill="#a9d26f"/>
      <polygon points="0,2.5 76,2.5 73,10 0,10" fill="url(#greenFade)"/>
      <polygon points="77,2.5 100,2.5 100,10 74,10" fill="#1f6fa8"/>
    </symbol>
  </defs>
</svg>

<section class="sheet letterhead">
  <div class="brand"><span class="brand-square"></span><span class="brand-name">Pemberton Hale Warrick</span></div>
  <div class="faint-mark"></div>
  <p class="contact">
    tel 417.555.0142 &nbsp;|&nbsp; fax 417.555.0143<br>
    dpemberton@pembertonhalewarrick.example<br>
    4738 E. Harrowgate Ave., Suite C-212B, Springfield, Missouri 65809
  </p>
  <svg class="band"><use href="#brand-band"/></svg>
  <p class="web">www.pembertonhalewarrick.example</p>
</section>

<section class="sheet card card-front">
  <div class="brand"><span class="brand-square"></span><span class="brand-name">Pemberton Hale Warrick</span></div>
  <p class="web">www.pembertonhalewarrick.example</p>
  <svg class="band"><use href="#brand-band"/></svg>
</section>

<section class="sheet card card-back">
  <div class="brand"><span class="brand-square"></span><span class="brand-name">Pemberton Hale Warrick</span></div>
  <p class="holder"><strong>Derek R. Pemberton, P.E.</strong> &nbsp;|&nbsp; Principal</p>
  <p class="contact">
    tel 417.555.0142 &nbsp; fax 417.555.0143<br>
    dpemberton@pembertonhalewarrick.example<br>
    4738 E. Harrowgate Ave., Suite C-212B, Springfield, Missouri 65809
  </p>
  <svg class="band"><use href="#brand-band"/></svg>
</section>

<section class="sheet envelope-flap">
  <svg class="fold" viewBox="0 0 468 250" preserveAspectRatio="none">
    <polyline points="0,2 200,78 268,78 468,2" fill="none" stroke="var(--fold)" stroke-width="1"/>
  </svg>
  <span class="brand-square"></span>
</section>

<section class="sheet envelope-dl">
  <div class="brand"><span class="brand-square"></span><span class="brand-name">Pemberton Hale Warrick</span></div>
  <div class="faint-mark"></div>
  <p class="contact">
    tel 417.555.0142 &nbsp;|&nbsp; fax 417.555.0143<br>
    dpemberton@pembertonhalewarrick.example<br>
    4738 E. Harrowgate Ave., Suite C-212B, Springfield, Missouri 65809
  </p>
  <svg class="band"><use href="#brand-band"/></svg>
</section>

</body>
</html>
```